Box Design of "pet rapid test for dogs & cats" with professional use

"The market is in Southeast Asia, South America, Europe, and the U.S."
Clients: Veterinary clinics, pet hospitals,(a small number of home use)

Primary colors:
Orange, Green,or Blue, (select 1,or 2 color)
Neutrals: Black, Gray, or White (optional)
Dimensions:135mm(L)*90mm(W)*105mm(W)

Kindly review the attached file for additional content
Updates

I have increased my budget, please provide a satisfactory design solution, thank you very much for your work.

Target Market(s)

Southeast Asia, South America, Europe, and the U.S.

Industry/Entity Type

Veterinary test kit for dogs & cats

Colors
0054AA
0677BA
7BADD7
CADEEF
E8F1F8
0094D4
00A9DD
6FCCEA
C7EBF8
E9F6FB
00AB8E
00BBA5
67D7C9
C6EFE9
E9F9F6
59FF00
82FF00
B8FF75
E3FFCB
F4FFEA
F0912C
F2A743
F7CA91
FBE8D2
FDF5EE
EE7325
F08F49
F5BC92
FAE3D3
FDF4ED

Requirements
Nice to have
• Appealing Box Appearance with professional

```html
<!DOCTYPE html>
<html lang="en">
<head>
<meta charset="utf-8">
<title>Pet Rapid Test Kit – Box Dieline</title>
<link rel="stylesheet" href="https://fonts.googleapis.com/css2?family=Archivo:wght@400;600;800&family=Inter:wght@400;500;600&display=swap">
<style>
  :root{
    --brand:#336699;
    --brand-deep:#2d5f93;
    --band-light:#6079a7;
    --band-tab:#7d92bb;
    --ink-line:#1a1a1a;
    --paper:#ffffff;
  }
  *{margin:0;padding:0;box-sizing:border-box}
  html,body{width:1200px;height:675px;overflow:hidden;background:var(--paper)}
  .canvas{position:relative;width:1200px;height:675px;font-family:"Inter",sans-serif;color:var(--brand)}
  .dieline{position:absolute;left:0;top:0}
  .abs{position:absolute}
  .band-strip{left:181px;top:380px;width:839px;height:12px;background:var(--band-light)}
  .band-pattern{left:181px;top:392px;width:839px;height:46px;background:linear-gradient(90deg,var(--brand-deep),#3a6c9e 50%,var(--brand-deep))}
  .maker{top:382px;width:120px;text-align:center;color:#fff;font-size:3.6px;font-weight:600;line-height:1.25}
  .maker small{display:block;font-size:2.3px;letter-spacing:.6px;opacity:.8;font-weight:400}
  .count-tab{top:392px;width:62px;height:13px;background:var(--band-tab);clip-path:polygon(0 0,100% 0,94% 100%,6% 100%);color:#fff;display:flex;align-items:center;justify-content:center;gap:3px;font-family:"Archivo",sans-serif}
  .count-tab b{font-size:8px;font-weight:800;letter-spacing:.5px}
  .count-tab span{font-size:4.5px;font-weight:600;letter-spacing:.6px;line-height:1;text-align:center}
  .count-tab span i{display:block;font-style:normal;font-size:2.4px;letter-spacing:2.4px}
  .side-tag{top:272px;height:16px;width:50px;background:var(--brand);color:#fff;font-family:"Archivo",sans-serif;font-size:5.4px;font-weight:600;letter-spacing:.3px;display:flex;align-items:center;padding-left:10px}
  .feature-list{left:194px;top:291px;width:145px;list-style:none;font-size:4.6px;line-height:6.45px}
  .feature-list .head{font-weight:500;padding-left:6px;position:relative}
  .feature-list .head::before{content:"";position:absolute;left:0;top:1.6px;width:3.2px;height:3.2px;background:var(--brand)}
  .feature-list .tick{padding-left:6px;position:relative;font-weight:400}
  .feature-list .tick::before{content:"✓";position:absolute;left:0;font-size:3.6px}
  .feature-list .cont{padding-left:6px}
  .brand-lockup{display:flex;align-items:center;gap:5px}
  .brand-dot{width:16px;height:16px;border-radius:50%;background:var(--brand)}
  .brand-name{font-family:"Archivo",sans-serif;font-weight:600;font-size:8px;letter-spacing:.4px;color:var(--brand)}
  .title{font-family:"Archivo",sans-serif;line-height:1}
  .title .t1{font-size:13px;letter-spacing:.3px}
  .title .t1 b{font-weight:800}
  .title .t1 span{font-weight:400}
  .title .t2{font-size:7.8px;font-weight:600;margin-top:2px;letter-spacing:.3px}
  .title .t3{font-size:6.6px;font-weight:400;margin-top:2px;letter-spacing:.5px;padding-left:1px}
  .contents{font-size:4.7px;line-height:1}
  .contents p{position:absolute;white-space:nowrap}
  .icons{display:flex;align-items:center;gap:7px}
  .ivd{border:1.2px solid var(--brand);font-family:"Archivo",sans-serif;font-weight:800;font-size:7px;padding:0 2px;line-height:8px}
  .benefits{left:594px;top:292px;width:138px;font-size:4.6px;line-height:6px}
</style>
</head>
<body>
<div class="canvas">

  <svg class="dieline" width="1200" height="675" viewBox="0 0 1200 675" fill="none" stroke="var(--ink-line)" stroke-width=".7">
    <rect x="181" y="263" width="803" height="187"/>
    <line x1="342" y1="263" x2="342" y2="450"/>
    <line x1="582" y1="263" x2="582" y2="450"/>
    <line x1="743" y1="263" x2="743" y2="450"/>
    <path d="M984 263 L1020 269 V445 L984 450"/>
    <path d="M181 263 L186 258 V192 H316 Q333 192 333 209 L338 256 L342 258 V263"/>
    <path d="M582 263 V258 L587 256 L591 209 Q591 192 608 192 H739 V258 L743 263"/>
    <path d="M743 263 V88 Q743 67 764 67 H962 Q984 67 984 88 V263"/>
    <line x1="743" y1="102" x2="984" y2="102"/>
    <path d="M181 450 L261 503 V526 Q261 539 275 539 H342 V450"/>
    <path d="M342 450 L395 530 V553 Q395 566 408 566 H516 Q529 566 529 553 V530 L582 450"/>
    <path d="M582 450 V539 H650 Q663 539 663 526 V503 L743 450"/>
    <path d="M743 450 V566 H783 Q796 566 796 553 V530 H930 V553 Q930 566 943 566 H984 V450"/>
  </svg>

  <div class="abs band-strip"></div>
  <div class="abs band-pattern" role="img" aria-label="Band of soft paw-print pattern in blue tones"></div>

  <div class="abs maker" style="left:201px">MADE by NORVAL LABS<small>LOVED BY PETS, TRUSTED BY VET</small></div>
  <div class="abs maker" style="left:603px">MADE by NORVAL LABS<small>LOVED BY PETS, TRUSTED BY VET</small></div>

  <div class="abs count-tab" style="left:371px"><b>10</b><span>TESTS<i>BOX</i></span></div>
  <div class="abs count-tab" style="left:771px"><b>10</b><span>PRUEBAS<i>POR CAJA</i></span></div>

  <!-- side panel: Spanish features -->
  <div class="abs side-tag" style="left:181px">TAILWELL</div>
  <ul class="abs feature-list">
    <li class="head">Fácil y Práctico:</li>
    <li class="tick">Sin capacitación previa</li>
    <li class="tick">Suficientemente simple para uso en casa</li>
    <li class="head">RÁPIDO Y EFICIENTE:</li>
    <li class="tick">Resultados digitales en &lt;10 minutos</li>
    <li class="tick">Desde inicio hasta resultado final</li>
    <li class="head">PRECISO Y FIABLE:</li>
    <li class="tick">Resultados rápidos y confiables con tecnología de</li>
    <li class="tick">inmunocromatografía avanzada</li>
    <li class="cont">Validado por clínicas veterinarias a nivel global</li>
    <li class="head">DETECCIÓN MULTIENFERMEDADES:</li>
    <li class="tick">Evalúa múltiples patologías simultáneamente</li>
    <li class="tick">Ayuda a los dueños a detectar problemas a tiempo</li>
  </ul>

  <!-- front panel: English -->
  <div class="abs brand-lockup" style="left:360px;top:278px">
    <div class="brand-dot"></div>
    <div class="brand-name">TAILWELL</div>
  </div>
  <div class="abs title" style="left:360px;top:305px">
    <div class="t1"><b>PET</b> <span>RAPID</span></div>
    <div class="t2">TEST KIT FOR</div>
    <div class="t3">DOGS &amp; CATS</div>
  </div>
  <div class="abs contents" style="left:360px;top:346px;width:220px;height:30px">
    <p style="left:0;top:0">(1)- Test Kits(Cassette,disposable dropper,desiccant)</p>
    <p style="left:0;top:10px">(2)- Sterile swabs</p>
    <p style="left:53px;top:10px">(4)- Instruction manual</p>
    <p style="left:0;top:20px">(3)- Assay buffer</p>
    <p style="left:53px;top:21px">(5)- Store at 2~30℃</p>
  </div>
  <div class="abs icons" style="left:485px;top:358px">
    <div class="ivd">IVD</div>
    <svg width="16" height="14" viewBox="0 0 16 14" stroke="var(--brand)" fill="none" stroke-width=".8"><path d="M3 10 L7 8 M7 13 V2 H12"/><circle cx="7" cy="12.5" r="1" fill="var(--brand)"/></svg>
    <svg width="12" height="14" viewBox="0 0 12 14" stroke="var(--brand)" fill="none" stroke-width=".8"><circle cx="6" cy="6" r="2.2"/><path d="M6 0.5V2.5M6 9.5V11.5M0.5 6H2.5M9.5 6H11.5M2 2L3.4 3.4M8.6 8.6L10 10M2 10L3.4 8.6M8.6 3.4L10 2"/></svg>
    <svg width="12" height="10" viewBox="0 0 12 10" stroke="var(--brand)" fill="none" stroke-width=".8"><path d="M1 1.5H5L6 2.5L7 1.5H11V9H7L6 8.2L5 9H1Z M6 2.5V8.2"/><path d="M8.5 4V7.5"/></svg>
    <svg width="13" height="13" viewBox="0 0 13 13" stroke="var(--brand)" fill="none" stroke-width=".9"><circle cx="6.5" cy="6.5" r="5.7"/><path d="M4 3.5Q6.5 2.5 7 5Q7.5 7.5 9.5 8M4.5 9.5L8.5 5M2.5 2.5L10.5 10.5"/></svg>
  </div>

  <!-- back panel: English benefits -->
  <div class="abs side-tag" style="left:582px">TAILWELL</div>
  <p class="abs benefits">Simple &amp; Convenient: no professional skills required, Simple enough for home use.<br>Fast &amp; Efficient: Digital results in &lt; 10 minutes- from start to completion.<br>Accurate &amp; Reliable: Quick and trustworthy pet health results using advanced lateral flow biotech, Trusted by vet clinics worldwide.<br>Supports screening of multiple diseases, Helping pet owners detect issues early.</p>

  <!-- front panel: Spanish -->
  <div class="abs brand-lockup" style="left:762px;top:278px">
    <div class="brand-dot"></div>
    <div class="brand-name">TAILWELL</div>
  </div>
  <div class="abs title" style="left:762px;top:305px">
    <div class="t1"><b>KIT DE</b> <span>PRUEBA</span></div>
    <div class="t2">RÁPIDA PARA MASCOTAS</div>
    <div class="t3">PERROS Y GATOS</div>
  </div>
  <div class="abs contents" style="left:762px;top:346px;width:220px;height:30px">
    <p style="left:0;top:0">(1)- Kits de prueba (cassette, gotero desechable, desecante)</p>
    <p style="left:0;top:10px">(2)- Buffer de ensayo</p>
    <p style="left:53px;top:10px">(4)- Manual de instrucciones</p>
    <p style="left:0;top:20px">(3)- Hisopos estériles</p>
    <p style="left:53px;top:21px">(5)- Almacenamiento: 2~30℃</p>
  </div>
  <div class="abs icons" style="left:886px;top:358px">
    <div class="ivd">IVD</div>
    <svg width="16" height="14" viewBox="0 0 16 14" stroke="var(--brand)" fill="none" stroke-width=".8"><path d="M3 10 L7 8 M7 13 V2 H12"/><circle cx="7" cy="12.5" r="1" fill="var(--brand)"/></svg>
    <svg width="12" height="14" viewBox="0 0 12 14" stroke="var(--brand)" fill="none" stroke-width=".8"><circle cx="6" cy="6" r="2.2"/><path d="M6 0.5V2.5M6 9.5V11.5M0.5 6H2.5M9.5 6H11.5M2 2L3.4 3.4M8.6 8.6L10 10M2 10L3.4 8.6M8.6 3.4L10 2"/></svg>
    <svg width="12" height="10" viewBox="0 0 12 10" stroke="var(--brand)" fill="none" stroke-width=".8"><path d="M1 1.5H5L6 2.5L7 1.5H11V9H7L6 8.2L5 9H1Z M6 2.5V8.2"/><path d="M8.5 4V7.5"/></svg>
    <svg width="13" height="13" viewBox="0 0 13 13" stroke="var(--brand)" fill="none" stroke-width=".9"><circle cx="6.5" cy="6.5" r="5.7"/><path d="M4 3.5Q6.5 2.5 7 5Q7.5 7.5 9.5 8M4.5 9.5L8.5 5M2.5 2.5L10.5 10.5"/></svg>
  </div>

</div>
</body>
</html>
```